Construction Company Needs Letterhead Design

We recently had a new logo designed and would like to have our letterhead updated to a trendier design. We are a concrete construction company based out of Iowa, but do work for Agricultural businesses across the Midwest.

Industry/Entity Type

Construction

Colors
ec1f27
000000
ffffff

Requirements
Must have
• Must stay within our current color scheme of red/black/white. Must have have our address, phone number, e-mail address, etc. printed on the letterhead as well.

```html
<!DOCTYPE html>
<html lang="en">
<head>
<meta charset="utf-8">
<title>Harwick Field Services Letterhead</title>
<link rel="stylesheet" href="https://fonts.googleapis.com/css2?family=Questrial&family=Roboto:wght@400;700&display=swap">
<style>
  :root{
    --brand-red:#ec1f27;
    --brand-black:#1a1a1a;
    --paper:#f3f3f3;
    --paper-edge:#e4e4e4;
    --backdrop:#e2e2e2;
    --ink:#4a4a4a;
    --ink-soft:#5c5c5c;
    --white:#ffffff;
  }
  *{box-sizing:border-box;margin:0;padding:0}
  html,body{width:1024px;height:1200px;overflow:hidden}
  body{background:var(--backdrop);position:relative;font-family:"Questrial",sans-serif}
  .letterhead{
    position:absolute;left:105px;top:30px;width:814px;height:1140px;
    background:linear-gradient(180deg,var(--white) 0%,var(--paper) 55%,var(--paper-edge) 100%);
    box-shadow:0 4px 18px rgba(0,0,0,.12);overflow:hidden;
  }
  .header-art{position:absolute;left:0;top:0;width:814px;height:340px}
  .contact{
    position:absolute;right:32px;top:26px;text-align:right;color:var(--white);
    font-family:"Roboto",sans-serif;font-size:13px;line-height:16px;
  }
  .contact .address{margin-bottom:8px}
  .contact .row{display:flex;justify-content:flex-end;align-items:center;gap:8px}
  .contact svg{width:10px;height:10px;fill:var(--brand-red)}
  .brand{position:absolute;left:77px;top:124px;display:flex;align-items:center;gap:10px}
  .brand-mark{width:30px;height:30px;background:var(--brand-red)}
  .brand-name{font-family:"Roboto",sans-serif;font-weight:700;font-size:34px;letter-spacing:1px;color:var(--brand-black)}
  .letter{position:absolute;left:77px;top:402px;width:670px;color:var(--ink)}
  .salutation{font-size:20px;color:var(--ink-soft);margin-bottom:34px}
  .letter p{font-size:11.4px;line-height:14.6px;margin-bottom:15px;text-align:justify}
  .closing{margin-top:36px}
  .signature{
    margin-top:30px;width:140px;height:60px;border-radius:4px;
    background:linear-gradient(90deg,rgba(40,80,170,.18),rgba(40,80,170,.05));
  }
  .watermark-area{
    position:absolute;left:0;bottom:0;width:814px;height:430px;
    background:radial-gradient(ellipse at 55% 20%,rgba(236,31,39,.05),rgba(0,0,0,.03) 60%,transparent 80%);
  }
</style>
</head>
<body>
  <main class="letterhead">
    <div class="watermark-area" role="img" aria-label="Faint decorative background wash"></div>

    <svg class="header-art" viewBox="0 0 666 278" preserveAspectRatio="none" aria-hidden="true">
      <path d="M0 0 H666 V177 C560 90 400 30 270 36 C160 42 70 78 0 122 Z" fill="#1a1a1a"/>
      <path d="M0 122 C70 78 160 42 270 36 C400 30 500 70 580 120 C480 72 380 46 270 48 C165 52 75 90 0 134 Z" fill="#ec1f27"/>
    </svg>

    <address class="contact">
      <div class="address">PO Box 318 Dunmore<br>Iowa 50421</div>
      <div class="row">(515) 555.0142 <svg viewBox="0 0 10 10"><path d="M2 0h2l1 3-1.5 1a6 6 0 0 0 2.5 2.5L7 5l3 1v2c0 1-1 2-2 2A8 8 0 0 1 0 2c0-1 1-2 2-2z"/></svg></div>
      <div class="row">info@harwickfield.com <svg viewBox="0 0 10 10"><path d="M0 2h10v1L5 6 0 3zM0 4l5 3 5-3v4H0z"/></svg></div>
      <div class="row">www.harwickfield.com <svg viewBox="0 0 10 10"><circle cx="5" cy="5" r="5"/></svg></div>
    </address>

    <div class="brand">
      <span class="brand-mark"></span>
      <span class="brand-name">HARWICK</span>
    </div>

    <section class="letter">
      <h1 class="salutation" style="font-weight:400">Dear Mr. Reed,</h1>
      <p>Lorem ipsum dolor sit amet, consectetur adipiscing elit. Donec orci purus, luctus vitae dignissim eu, iaculis sed purus. Vivamus faucibus, ipsum nec aliquet viverra, leo mauris condimentum ligula, sit amet sagittis enim ligula quis arcu. Nam egestas tortor id nisi porttitor mattis. In tortor ante, ultricies in suscipit a, tempus non massa. Vivamus et auctor mi. Fusce vel massa nulla. Phasellus nec eros mauris, et scelerisque orci.</p>
      <p>Donec malesuada orci vitae nulla accumsan porta a id massa. Quisque accumsan iaculis magna sit amet fringilla. Maecenas consequat, magna eget tincidunt semper, odio nibh rutrum mi, id feugiat ante nisi eu risus. Vestibulum nunc orci, rhoncus a placerat in, ultricies in mi. Cras mattis varius eros, vel fringilla nisi suscipit eget. Quisque scelerisque sagittis nulla at porttitor.</p>
      <p>Sed id augue vitae urna euismod commodo aliquet a quam. Pellentesque arcu velit, cursus et malesuada ut, consequat et diam. Nullam erat sem, rhoncus id ullamcorper vitae, rhoncus et arcu. In ultricies ultricies nulla, ut rutrum nisi iaculis at. Donec eu magna a metus ornare faucibus. Fusce aliquet faucibus ultricies. Morbi semper, est id tincidunt gravida, sem arcu adipiscing lacus, ac bibendum nulla leo eu purus. Quisque nec diam sed risus consectetur accumsan quis quis nibh. Vestibulum id purus lorem.</p>
      <p>It is a long established fact that a reader will be distracted by the readable content of a page when looking at its layout. The point of using Lorem Ipsum is that it has a more-or-less normal distribution of letters, as opposed to using 'Content here, content here', making it look like readable English. Many desktop publishing packages</p>
      <p class="closing">Sincerely,</p>
      <div class="signature" role="img" aria-label="Handwritten signature of Paul Reed"></div>
    </section>
  </main>
</body>
</html>
```